Estou muito feliz om o resultado final do trabalho de vocês gostaria de agradecer a toda a equipe que me ajudou na construção desse projeto. Parabenizar em especial o MARCELO do 0800... muito solicito presta um ótimo atendimento.

```html
<!DOCTYPE html>
<html lang="pt-BR">
<head>
<meta charset="utf-8">
<title>Everton Marcelo – Papel timbrado</title>
<link href="https://fonts.googleapis.com/css2?family=Open+Sans:wght@400;600;700;800&display=swap" rel="stylesheet">
<style>
  :root {
    --backdrop: #2c2c2e;
    --paper: #f7f7f7;
    --ink: #3a3a3a;
    --ink-soft: #6b6b6b;
    --brand-red: #c8161d;
    --brand-red-dark: #9e0f15;
    --watermark: #ececec;
    --white: #ffffff;
  }
  * { box-sizing: border-box; margin: 0; padding: 0; }
  html, body {
    width: 1200px; height: 1200px; overflow: hidden;
    background: var(--backdrop);
    font-family: "Open Sans", Arial, sans-serif;
  }
  .stage {
    width: 1200px; height: 1200px;
    display: flex; align-items: center; justify-content: center;
  }
  .letterhead {
    position: relative;
    width: 780px; height: 1104px;
    background: var(--paper);
    overflow: hidden;
  }
  .watermark {
    position: absolute;
    left: 300px; top: 330px;
    width: 300px; height: 300px;
    border-radius: 50%;
    background: var(--watermark);
  }
  .brand {
    position: absolute; top: 60px; right: 70px;
    display: flex; align-items: center; gap: 10px;
  }
  .brand-dot {
    width: 16px; height: 16px; border-radius: 50%;
    background: var(--brand-red);
  }
  .brand-text { text-align: left; line-height: 1.05; }
  .brand-name {
    font-size: 24px; font-weight: 800; color: var(--ink);
  }
  .brand-role {
    font-size: 12px; font-weight: 700; color: var(--ink);
  }
  .content {
    position: absolute; top: 170px; left: 80px; right: 80px;
    color: var(--ink-soft); font-size: 15px; line-height: 1.6;
  }
  .greeting { margin-bottom: 36px; }
  .content p.body { margin-bottom: 26px; text-align: left; }
  .footer {
    position: absolute; left: 0; right: 0; bottom: 0; height: 120px;
  }
  .footer-band { position: absolute; inset: 0; width: 100%; height: 100%; }
  .footer-info {
    position: absolute; left: 40px; bottom: 26px;
    color: var(--white); font-size: 11px; line-height: 1.7;
  }
  .footer-info .web { font-size: 15px; font-weight: 600; }
  .footer-row { display: flex; gap: 18px; }
  .footer-brand {
    position: absolute; right: 40px; bottom: 32px;
    display: flex; align-items: center; gap: 6px;
    color: var(--white); font-weight: 800; font-size: 14px;
  }
  .footer-brand .brand-dot { background: var(--white); width: 10px; height: 10px; }
</style>
</head>
<body>
<main class="stage">
  <article class="letterhead">
    <div class="watermark" aria-hidden="true"></div>

    <header class="brand">
      <span class="brand-dot"></span>
      <div class="brand-text">
        <div class="brand-name">Everton Marcelo</div>
        <div class="brand-role">Personal Trainer</div>
      </div>
    </header>

    <section class="content">
      <p class="greeting">Lorem ipsum dolor sit</p>
      <p class="body">Lorem ipsum dolor sit amet, consectetur adipiscing elit, sed diam nonummy nibh euismod tincidunt ut laoreet dolore magna aliquam erat volutpat. Ut wisi enim ad minim veniam, quis nostrud exerci tation ullamcorper suscipit lobortis nisl ut aliquip ex ea commodo consequat. Duis autem vel eum iriure dolor in hendrerit in vulputate velit esse molestie consequat, vel illum dolore eu feugiat nulla facilisis.</p>
      <p class="body">Lorem ipsum dolor sit amet, consectetur adipiscing elit, sed diam nonummy nibh euismod tincidunt ut laoreet dolore magna aliquam erat volutpat. Ut wisi enim ad minim veniam, quis nostrud exerci tation ullamcorper suscipit lobortis nisl ut aliquip ex ea commodo consequat. Duis autem vel eum iriure dolor in hendrerit in vulputate velit esse molestie consequat, vel illum dolore eu feugiat nulla facilisis.</p>
      <p class="body">Lorem ipsum dolor sit amet, consectetur adipiscing elit, sed diam nonummy nibh euismod tincidunt ut laoreet dolore magna aliquam erat volutpat. Ut wisi enim ad minim veniam, quis nostrud exerci tation ullamcorper suscipit lobortis nisl ut aliquip ex ea commodo consequat. Duis autem vel eum iriure dolor in hendrerit in vulputate velit esse molestie consequat, vel illum dolore eu feugiat nulla facilisis.</p>
    </section>

    <footer class="footer">
      <svg class="footer-band" viewBox="0 0 780 120" preserveAspectRatio="none" aria-hidden="true">
        <path d="M0 30 L560 30 C640 30 680 0 780 0 L780 120 L0 120 Z" fill="var(--brand-red)"/>
        <path d="M0 30 L560 30 C640 30 680 0 780 0 L780 6 C686 6 646 36 560 36 L0 36 Z" fill="var(--brand-red-dark)"/>
      </svg>
      <div class="footer-info">
        <div>Rua das Palmeiras, 120 - Centro - Cuiabá/MT - CEP 78.010-120</div>
        <div class="footer-row">
          <span>contato@evertonmarcelo.com.br</span>
          <span>/evertonmarcelo</span>
          <span>(65) 3000-1200</span>
        </div>
        <div class="web">www.evertonmarcelo.com.br</div>
      </div>
      <div class="footer-brand">
        <span class="brand-dot"></span>
        <span>Everton Marcelo</span>
      </div>
    </footer>
  </article>
</main>
</body>
</html>
```